Horizon of Bright Tomorrows, LLC needs business stationary designed using our logo.

Horizon of Bright Tomorrows is a new life coaching business. We have a logo design . We need a design for stationary for branding a new PathCrafter Life Coach business. We help people transform their lives by exploring, designing and taking action steps for the life they love in the areas of health and wellness, relationships, vocation, and time and money freedom. We like bright happy colors that present growth and transformation and also compliments the blue logo design.

Hello Designers, Thank you for accepting my design request. I wanted to be sure I put all the information for the business stationary design. If this is already in the order please disregard. Information to incorporate into stationary design Logo: incorporate blues and complimentary color Company name: Horizon of Bright Tomorrows, LLC Tagline: Transformational Life Coaching "If you can think it, you can do it You CAN live a life you LOVE! Website: www.marisolpenwick.PathCrafterGuide.example Email: marisolpenwick@PathCrafterGuide.example P.O. Box 5927 Edcouch, TX 78561 555-317-9042 Marisol T. Penwick, Certified PathCrafter* Coach Positive, upbeat, professional design Thank you.

Industry/Entity Type

Life Coaching

Font styles to use
Decorative

Colors
0355a3

Requirements
Must have
• Information to incorporate into stationary design
• Logo: incorporate blues and complimentary color
• Company name: Horizon of Bright Tomorrows, LLC
• Tagline: Transformational Life Coaching
• "If you can think it, you can do it You CAN live a life you LOVE!
• Website: www.marisolpenwick.PathCrafterGuide.example
• Email: marisolpenwick@PathCrafterGuide.example
• P.O. Box 5927 Edcouch, TX 78561 555-317-9042
• Marisol T. Penwick, Certified PathCrafter* Coach
• Positive, upbeat, professional design
Nice to have
• Watermark
Should not have
• No negativity or negative vibes
• Nothing derogatory
• No clashing colors

```html
<!DOCTYPE html>
<html lang="en">
<head>
<meta charset="utf-8">
<title>Horizon of Bright Tomorrows — Stationery</title>
<link href="https://fonts.googleapis.com/css2?family=Didact+Gothic&family=Montserrat:wght@400;600;800&display=swap" rel="stylesheet">
<style>
:root{
  --bg:#9e9e9e;
  --paper:#f4f4f5;
  --paper-edge:#e6e6e8;
  --brand:#2a12d6;
  --brand-deep:#2410c8;
  --brand-violet:#5a2a9e;
  --ink:#4a4a55;
  --ink-soft:#6b6b76;
  --white:#ffffff;
}
*{box-sizing:border-box;margin:0;padding:0}
html,body{width:1200px;height:899px;overflow:hidden;background:var(--bg)}
body{position:relative;font-family:"Didact Gothic",sans-serif;color:var(--ink)}
.sheet{position:absolute;background:var(--paper)}
.brand-name{font-family:"Montserrat",sans-serif;font-weight:800;color:var(--brand);white-space:nowrap}
.brand-dot{display:block;border-radius:50%;background:var(--brand)}
.brand-lockup{display:flex;flex-direction:column;align-items:center}
.tagline{font-size:4.5px;color:var(--ink-soft);letter-spacing:.1px}

/* letterhead */
.letterhead{left:153px;top:81px;width:377px;height:531px;overflow:hidden}
.letterhead .brand-lockup{position:absolute;left:0;right:0;top:30px}
.letterhead .brand-dot{width:26px;height:26px;margin-bottom:4px}
.letterhead .brand-name{font-size:6.8px}
.watermark{position:absolute;left:128px;top:290px;width:150px;height:150px;border-radius:50%;background:var(--brand);opacity:.04}
.salutation{position:absolute;left:33px;top:149px;font-size:10px;color:var(--ink)}
.letter-body{position:absolute;left:33px;top:178px;width:315px;font-size:5.4px;line-height:8.2px;color:var(--ink-soft)}
.letter-body p{margin-bottom:8px}
.signature{position:absolute;left:30px;top:368px;width:88px;height:28px;border-radius:14px;background:linear-gradient(90deg,rgba(42,18,214,.16),rgba(42,18,214,.04))}
.closing{position:absolute;left:33px;top:348px;font-size:5.4px;color:var(--ink-soft)}
.letter-footer{position:absolute;left:93px;top:496px;display:flex;gap:14px;font-family:"Montserrat",sans-serif;font-size:5px;line-height:7.2px;color:var(--ink)}
.contact-row{display:flex;align-items:center;gap:3px}
.icon{width:5px;height:5px;flex:none}

/* folder */
.folder{left:564px;top:48px;width:445px;height:565px;background:radial-gradient(circle at 50% 49%,#2b10e8 0,#3a17d0 22%,#5a2aa6 42%,#4a22b8 65%,#2d13d2 100%)}
.folder-spine{position:absolute;top:0;bottom:0;width:1px;background:rgba(255,255,255,.28)}
.folder .brand-lockup{position:absolute;left:0;right:0;top:210px}
.folder .brand-dot{width:52px;height:52px;background:var(--white);margin-bottom:14px}
.folder .brand-name{color:var(--white);font-size:17px}

/* business cards */
.card-front{left:66px;top:656px;width:156px;height:90px;background:radial-gradient(circle at 50% 45%,#3a14e6 0,#4a22b8 55%,#3a18c8 100%)}
.card-front .brand-lockup{position:absolute;left:0;right:0;top:22px}
.card-front .brand-dot{width:18px;height:18px;background:var(--white);margin-bottom:4px}
.card-front .brand-name{color:var(--white);font-size:5px}
.card-url{position:absolute;left:0;right:0;top:71px;text-align:center;font-family:"Montserrat",sans-serif;font-size:3.6px;letter-spacing:2.2px;color:var(--white)}
.card-back{left:67px;top:762px;width:156px;height:90px;background:var(--white)}
.card-back .brand-lockup{position:absolute;left:60px;width:90px;top:13px}
.card-back .brand-dot{width:13px;height:13px;margin-bottom:3px}
.card-back .brand-name{font-size:3.3px}
.card-back .tagline{font-size:2.6px}
.person{position:absolute;left:9px;top:54px;font-family:"Montserrat",sans-serif;color:var(--brand)}
.person-name{font-size:5.4px;font-weight:600}
.person-role{font-size:3.8px}
.card-rule{position:absolute;left:9px;right:9px;top:67px;height:.6px;background:#c9c9d2}
.card-contacts{position:absolute;left:9px;top:71px;display:flex;gap:5px;font-family:"Montserrat",sans-serif;font-size:3.2px;line-height:4.8px;color:var(--ink)}
.card-contacts .icon{width:3.4px;height:3.4px}

/* envelopes */
.envelope-front{left:242px;top:656px;width:436px;height:198px;background:var(--paper)}
.envelope-front .brand-lockup{position:absolute;left:21px;width:124px;top:25px}
.envelope-front .brand-dot{width:22px;height:22px;margin-bottom:4px}
.envelope-front .brand-name{font-size:5.4px}
.envelope-front .tagline{font-size:3.6px}
.return-address{position:absolute;left:28px;top:64px;font-family:"Montserrat",sans-serif;font-size:4.4px;color:var(--ink)}
.envelope-back{left:700px;top:654px;width:436px;height:198px;background:var(--paper);overflow:hidden}
.envelope-flap{position:absolute;left:0;top:0;width:436px;height:62px}
.envelope-back .brand-lockup{position:absolute;left:0;right:0;top:12px}
.envelope-back .brand-dot{width:22px;height:22px;background:var(--white);margin-bottom:4px}
.envelope-back .brand-name{color:var(--white);font-size:5px}
</style>
</head>
<body>

<!-- Letterhead -->
<section class="sheet letterhead">
  <div class="watermark"></div>
  <div class="brand-lockup">
    <span class="brand-dot"></span>
    <span class="brand-name">Horizon of Bright Tomorrows, LLC</span>
    <span class="tagline">Transformational Coaching</span>
  </div>
  <p class="salutation">Dear Mr. Hollis,</p>
  <div class="letter-body">
    <p>Lorem ipsum dolor sit amet, consectetur adipiscing elit. Donec orci purus, luctus vitae dignissim eu, iaculis sed purus. Vivamus faucibus, ipsum nec aliquet viverra, leo mauris condimentum ligula, sit amet sagittis enim ligula quis arcu. Nam egestas tortor id nisi porttitor mattis. In tortor ante, ultricies in suscipit a, tempus non massa. Vivamus et auctor mi. Fusce vel massa nulla. Phasellus nec eros mauris, et scelerisque orci.</p>
    <p>Donec malesuada orci vitae nulla accumsan porta a id massa. Quisque accumsan iaculis magna sit amet fringilla. Maecenas consequat, magna eget tincidunt semper, odio nibh rutrum mi, id feugiat ante nisi eu risus. Vestibulum nunc orci, rhoncus a placerat in, ultricies in mi. Cras mattis varius eros, vel fringilla nisi suscipit eget. Quisque scelerisque sagittis nulla at porttitor.</p>
    <p>Sed id augue vitae urna euismod commodo aliquet a quam. Pellentesque arcu velit, cursus et malesuada ut, consequat et diam. Nullam erat sem, rhoncus id ullamcorper vitae, rhoncus et arcu. In ultricies ultricies nulla, ut rutrum nisi iaculis at. Donec eu magna a metus ornare faucibus. Fusce aliquet faucibus ultricies. Morbi semper, est id tincidunt gravida, sem arcu adipiscing lacus, ac bibendum nulla leo eu purus. Quisque nec diam sed risus consectetur a accumsan quis quis nibh. Vestibulum id purus lorem.</p>
    <p>It is a long established fact that a reader will be distracted by the readable content of a page when looking at its layout. The point of using Lorem Ipsum is that it has a more-or-less normal distribution of letters, as opposed to using 'Content here, content here', making it look like readable English. Many desktop publishing packages</p>
  </div>
  <p class="closing">Sincerely,</p>
  <div class="signature" role="img" aria-label="Handwritten signature of Dana Whitfield"></div>
  <footer class="letter-footer">
    <div>4410 Meadowlark Road<br>Juneau, Alaska 99801</div>
    <div>
      <div class="contact-row"><svg class="icon" viewBox="0 0 10 10"><path d="M2 1l2 2-1 1.5c.8 1.5 1.5 2.2 3 3L7.5 6l2 2-1.5 1.5C4 9 1 6 .5 1.5z" fill="var(--brand)"/></svg>555 204 7731</div>
      <div class="contact-row"><svg class="icon" viewBox="0 0 10 10"><rect x="2.5" y=".5" width="5" height="9" rx="1" fill="none" stroke="var(--brand)" stroke-width="1.3"/></svg>555 862 1409</div>
    </div>
    <div>
      <div class="contact-row"><svg class="icon" viewBox="0 0 10 10"><rect x=".5" y="2" width="9" height="6" fill="var(--brand)"/></svg>hello@brightname.example</div>
      <div class="contact-row"><svg class="icon" viewBox="0 0 10 10"><circle cx="5" cy="5" r="4.5" fill="var(--brand)"/></svg>www.brightname.example</div>
    </div>
  </footer>
</section>

<!-- Presentation folder -->
<section class="sheet folder">
  <span class="folder-spine" style="left:20px"></span>
  <span class="folder-spine" style="left:24px"></span>
  <div class="brand-lockup">
    <span class="brand-dot"></span>
    <span class="brand-name">Horizon of Bright Tomorrows, LLC</span>
  </div>
</section>

<!-- Business card, front -->
<section class="sheet card-front">
  <div class="brand-lockup">
    <span class="brand-dot"></span>
    <span class="brand-name">Horizon of Bright Tomorrows, LLC</span>
  </div>
  <p class="card-url">www.brightname.example</p>
</section>

<!-- Business card, back -->
<section class="sheet card-back">
  <div class="brand-lockup">
    <span class="brand-dot"></span>
    <span class="brand-name">Horizon of Bright Tomorrows, LLC</span>
    <span class="tagline">Transformational Coaching</span>
  </div>
  <div class="person">
    <p class="person-name">DANA WHITFIELD</p>
    <p class="person-role">CEO/FOUNDER</p>
  </div>
  <div class="card-rule"></div>
  <div class="card-contacts">
    <div>4410 Meadowlark Road<br>Juneau, Alaska 99801</div>
    <div>
      <div class="contact-row"><svg class="icon" viewBox="0 0 10 10"><path d="M2 1l2 2-1 1.5c.8 1.5 1.5 2.2 3 3L7.5 6l2 2-1.5 1.5C4 9 1 6 .5 1.5z" fill="var(--brand)"/></svg>555 204 7731</div>
      <div class="contact-row"><svg class="icon" viewBox="0 0 10 10"><rect x="2.5" y=".5" width="5" height="9" rx="1" fill="none" stroke="var(--brand)" stroke-width="1.3"/></svg>555 862 1409</div>
    </div>
    <div>
      <div class="contact-row"><svg class="icon" viewBox="0 0 10 10"><rect x=".5" y="2" width="9" height="6" fill="var(--brand)"/></svg>hello@brightname.example</div>
      <div class="contact-row"><svg class="icon" viewBox="0 0 10 10"><circle cx="5" cy="5" r="4.5" fill="var(--brand)"/></svg>www.brightname.example</div>
    </div>
  </div>
</section>

<!-- Envelope, front -->
<section class="sheet envelope-front">
  <div class="brand-lockup">
    <span class="brand-dot"></span>
    <span class="brand-name">Horizon of Bright Tomorrows, LLC</span>
    <span class="tagline">Transformational Coaching</span>
  </div>
  <p class="return-address">4410 Meadowlark Road, Juneau, Alaska 99801</p>
</section>

<!-- Envelope, back -->
<section class="sheet envelope-back">
  <svg class="envelope-flap" viewBox="0 0 436 62" aria-hidden="true">
    <defs>
      <linearGradient id="flapFill" x1="0" x2="1" y1="0" y2="0">
        <stop offset="0" stop-color="#2c12d8"/>
        <stop offset=".5" stop-color="#5a2aa2"/>
        <stop offset="1" stop-color="#3a18cc"/>
      </linearGradient>
    </defs>
    <path d="M0 0H436L430 40Q427 60 407 60H29Q9 60 6 40Z" fill="url(#flapFill)"/>
  </svg>
  <div class="brand-lockup">
    <span class="brand-dot"></span>
    <span class="brand-name">Horizon of Bright Tomorrows, LLC</span>
  </div>
</section>

</body>
</html>
```